New Business Card Design for a Payroll Concierge Company

I need a new business card design that is simple and includes my current information. I am a payroll concierge company that processes payroll for clients who employ household employees and I also manage my client's personal bills, financial records. I want to include my current logo and a logo for an association (PFHKT) I belong too on the front of my business card. I will include both my all my company logo files and the association logo files.

Target Market(s)

People who hire household employees, nannies, home health aides, butlers, maids, etc for wealthy individuals and senior citizens who need help in the home.

Industry/Entity Type

Financial Service

Contact Information for Business Card

Company logo

Name: Martin L. Vellacourt
Managing Director

Office number: 203-555-0148
Business Cell: 203-555-0173

Website: www.tallywagedesk.net
Email: Martin.Vellacourt@tallywagedesk.com

Company address:

17 Heron Lane
Suite 208
Wilton,CT 06412

Font styles to use
Serif
Sans Serif

Colors
3176b5
85cae6
cee9f5
33a6d7
d3d3d3
dbdbdb

Requirements
Must have
• I need to have my company logo and name, phone numbers, website, email, and address on the card. I also want the association logo on the card somewhere but not too big. Small enough to see the logo maybe on the top or bottom corner. Or some where on there card that it doesn't take away the design.
Nice to have
• i like the blue color in my logo, grey, please see must haves business card details.
Should not have
• PLEASE DO NOT USE THE BUSINESS CARD DESIGNS IN THE FILES I UPLOADED. I AM NOT INTERESTED IN THAT DESIGN. ALSO THE ADDRESS AND WEBSITE ARE INCORRECT ON THOSE DESIGNS. PLEASE USE THE UPDATED INFO ON BUSINESS CARD DETAILS

```html
<!DOCTYPE html>
<html lang="en">
<head>
<meta charset="utf-8">
<title>Tally Wage Desk — Business Card</title>
<link href="https://fonts.googleapis.com/css2?family=Roboto:wght@400;500;700&display=swap" rel="stylesheet">
<style>
  :root {
    --backdrop: #1f1f1f;
    --card-white: #f6f6f6;
    --brand-blue: #1f63b4;
    --brand-blue-light: #3176b5;
    --back-blue: #1b6fc4;
    --back-blue-deep: #1459a8;
    --text-grey: #3c3c3c;
    --rule-grey: #d3d3d3;
    --badge-grey: #b9b9b9;
  }
  * { box-sizing: border-box; margin: 0; padding: 0; }
  html, body { width: 1200px; height: 972px; overflow: hidden; }
  body {
    background: var(--backdrop);
    font-family: "Roboto", Arial, sans-serif;
    position: relative;
  }
  .card {
    position: absolute;
    left: 355px;
    width: 490px;
    height: 280px;
  }
  .card-front {
    top: 182px;
    background: var(--card-white);
    border-radius: 0 80px 0 80px;
  }
  .card-back {
    top: 510px;
    border-radius: 80px 0 80px 0;
    overflow: hidden;
  }
  .contact {
    position: absolute;
    right: 224px;
    top: 74px;
    text-align: right;
    color: var(--text-grey);
    font-size: 11.5px;
    line-height: 16px;
  }
  .contact-name {
    color: var(--brand-blue);
    font-weight: 700;
    font-size: 14px;
    line-height: 18px;
    text-transform: uppercase;
  }
  .contact-title { margin-bottom: 10px; }
  .label { color: var(--brand-blue); font-weight: 700; }
  .sep { margin: 0 4px; }
  .divider {
    position: absolute;
    left: 283px;
    width: 1px;
    background: var(--rule-grey);
  }
  .divider-top { top: 78px; height: 86px; }
  .divider-bottom { top: 226px; height: 22px; }
  .brand {
    position: absolute;
    left: 300px;
    width: 160px;
    top: 112px;
    text-align: center;
  }
  .brand-mark {
    display: inline-block;
    width: 14px;
    height: 14px;
    background: var(--brand-blue);
    margin-bottom: 8px;
  }
  .brand-name {
    color: var(--brand-blue);
    font-weight: 700;
    font-size: 20px;
    line-height: 22px;
    white-space: nowrap;
  }
  .brand-tagline {
    color: var(--brand-blue);
    font-weight: 700;
    font-size: 20px;
    line-height: 22px;
  }
  .association-badge {
    position: absolute;
    left: 190px;
    top: 228px;
    width: 78px;
    height: 20px;
    background: var(--badge-grey);
    border-radius: 2px;
  }
  .website {
    position: absolute;
    left: 307px;
    top: 230px;
    font-size: 11.5px;
    color: var(--text-grey);
  }
  .back-pattern {
    width: 100%;
    height: 100%;
    background: linear-gradient(135deg, var(--back-blue-deep), var(--back-blue) 55%, var(--brand-blue-light));
  }
</style>
</head>
<body>
  <section class="card card-front" aria-label="Business card front">
    <div class="contact">
      <p class="contact-name">Martin L. Vellacourt</p>
      <p class="contact-title">Managing Director</p>
      <p>17 Heron Lane, Suite 208, Wilton,CT 06412</p>
      <p><span class="label">M:</span> 203-555-0148<span class="sep">|</span><span class="label">T:</span> 203-555-0173</p>
      <p><span class="label">E:</span> Martin.Vellacourt@tallywagedesk.com</p>
    </div>
    <div class="divider divider-top"></div>
    <div class="brand">
      <span class="brand-mark"></span>
      <p class="brand-name">TALLY WAGE</p>
      <p class="brand-tagline">DESK</p>
    </div>
    <div class="association-badge" role="img" aria-label="Association membership badge"></div>
    <div class="divider divider-bottom"></div>
    <p class="website">www.tallywagedesk.net</p>
  </section>

  <section class="card card-back" aria-label="Business card back">
    <div class="back-pattern" role="img" aria-label="Repeating brand monogram pattern with a large embossed monogram on blue"></div>
  </section>
</body>
</html>
```